Varnel Group Limited Stationary

We are in need of business card and letterhead designs. We are looking for clean modern designs that complement the style and feel of our logo.

```html
<!DOCTYPE html>
<html lang="en">
<head>
<meta charset="utf-8">
<title>Varnel Group Limited – Business Card</title>
<link rel="stylesheet" href="https://fonts.googleapis.com/css2?family=Open+Sans:wght@400;600;700&display=swap">
<style>
  :root {
    --backdrop: #3b3430;
    --card: #141414;
    --card-edge: #222;
    --silver: #8e8e8e;
    --silver-light: #b4b4b4;
    --brand-blue: #1f5fb8;
    --ink: #f2f2f2;
    --rule: #5a5a5a;
  }
  * { margin: 0; padding: 0; box-sizing: border-box; }
  html, body { width: 1200px; height: 802px; overflow: hidden; }
  body {
    background: var(--backdrop);
    font-family: "Open Sans", Arial, sans-serif;
    position: relative;
  }
  .card {
    position: absolute;
    width: 520px;
    height: 297px;
    background: var(--card);
    border: 1px solid var(--card-edge);
    border-radius: 3px;
  }
  .card--front { left: 50px; top: 252px; }
  .card--back { left: 630px; top: 252px; }

  /* brand lockup */
  .brand {
    position: absolute;
    display: flex;
    flex-direction: column;
    align-items: center;
  }
  .brand__circle {
    border-radius: 50%;
    border: 3px solid var(--silver);
  }
  .brand__name {
    font-weight: 600;
    text-transform: uppercase;
    letter-spacing: 0.06em;
    white-space: nowrap;
  }
  .brand__rule {
    height: 1px;
    background: linear-gradient(90deg, transparent, var(--rule) 20%, var(--rule) 80%, transparent);
  }

  .card--front .brand { left: 0; right: 0; top: 62px; }
  .card--front .brand__circle { width: 62px; height: 62px; margin-bottom: 10px; }
  .card--front .brand__name { font-size: 38px; color: var(--silver); }
  .card--front .brand__rule { width: 300px; margin-top: 8px; }

  .card--back .brand { left: 180px; width: 300px; top: 22px; }
  .card--back .brand__circle { width: 46px; height: 46px; margin-bottom: 6px; border-color: var(--brand-blue); }
  .card--back .brand__name { font-size: 28px; color: var(--silver-light); }
  .card--back .brand__rule { width: 240px; margin-top: 6px; }

  /* contact block */
  .person {
    position: absolute;
    right: 285px;
    top: 140px;
    text-align: right;
    color: var(--ink);
  }
  .person__name {
    font-size: 20px;
    font-weight: 700;
    color: var(--brand-blue);
    margin-bottom: 6px;
    white-space: nowrap;
  }
  .person__line { font-size: 13.5px; line-height: 1.5; white-space: nowrap; }

  .divider {
    position: absolute;
    left: 250px;
    top: 170px;
    width: 1px;
    height: 100px;
    background: var(--silver);
  }

  .contacts {
    position: absolute;
    left: 264px;
    top: 168px;
    list-style: none;
    color: var(--ink);
  }
  .contacts__item {
    display: flex;
    align-items: center;
    gap: 8px;
    font-size: 14.5px;
    line-height: 21px;
    white-space: nowrap;
  }
  .contacts__icon { width: 10px; height: 10px; fill: var(--brand-blue); flex: none; }
</style>
</head>
<body>

  <section class="card card--front" aria-label="Business card front">
    <div class="brand">
      <span class="brand__circle"></span>
      <span class="brand__name">Varnel Group</span>
      <span class="brand__rule"></span>
    </div>
  </section>

  <section class="card card--back" aria-label="Business card back">
    <div class="brand">
      <span class="brand__circle"></span>
      <span class="brand__name">Varnel Group</span>
      <span class="brand__rule"></span>
    </div>

    <div class="person">
      <p class="person__name">Daniel R. Holloway</p>
      <p class="person__line">Managing Member</p>
      <p class="person__line">2280 Riverside Lane,</p>
      <p class="person__line">Fairmont, CA 95644</p>
    </div>

    <span class="divider"></span>

    <ul class="contacts">
      <li class="contacts__item">
        <svg class="contacts__icon" viewBox="0 0 10 10"><path d="M2 0.5 L3.6 2.6 L2.6 3.7 Q3.6 5.8 6.3 7.4 L7.4 6.4 L9.5 8 L8.3 9.5 Q3.8 9.2 0.5 1.7 Z"/></svg>
        (555) 214-3870
      </li>
      <li class="contacts__item">
        <svg class="contacts__icon" viewBox="0 0 10 10"><rect x="2.5" y="0.5" width="5" height="3"/><rect x="0.5" y="3.5" width="9" height="4" rx="1"/><rect x="2.5" y="6.5" width="5" height="3"/></svg>
        (555) 214-3871
      </li>
      <li class="contacts__item">
        <svg class="contacts__icon" viewBox="0 0 10 10"><path d="M2.5 0 H7.5 V10 H2.5 Z M3.3 1 V8 H6.7 V1 Z"/></svg>
        (555) 907-4412
      </li>
      <li class="contacts__item">
        <svg class="contacts__icon" viewBox="0 0 10 10"><path d="M0.5 2 H9.5 V8.5 H0.5 Z"/><path d="M0.5 2 L5 5.6 L9.5 2" stroke="#141414" stroke-width="0.9" fill="none"/></svg>
        daniel@harborlinedev.com
      </li>
      <li class="contacts__item">
        <svg class="contacts__icon" viewBox="0 0 10 10"><circle cx="5" cy="5" r="4.5"/><path d="M0.5 5 H9.5 M5 0.5 V9.5 M1.5 2.8 H8.5 M1.5 7.2 H8.5" stroke="#141414" stroke-width="0.7"/></svg>
        www.harborlinedev.com
      </li>
    </ul>
  </section>

</body>
</html>
```